Mandarin tuition, language and travel services

We need a website for a new startup company, which offers Mandarin tuition, translating and interpreting, and travel services. Our company is based in Jersey, a British channel island. We would like a creative and modern professional website. Preferably with some animations. The attached is a website, which style we would prefer:
http://www.morvaliqa.com/
We have also attached our logo for your reference
We would also like to see designs using black, red and orange, which corresponds with our logo colours. The cartoon images could be travel resorts in China, and the president of China waving to the web-browsers. Of course, we wouldn't wish to restrain the designers creativity. Any creative and interesting ideas are welcomed! We look forward to hearing from you!

Target Market(s)

school children and adults

Industry/Entity Type

It Company

Number of Pages Required

3 page

Requirements
Must have
• We would prefer a small 3 pages website, if possible. The 3 pages need to be Services, News Room, and Contact us.

```html
<!DOCTYPE html>
<html lang="en">
<head>
<meta charset="utf-8">
<title>Jadeway Mandarin</title>
<link rel="stylesheet" href="https://fonts.googleapis.com/css2?family=Cutive&family=Caveat&family=Cabin+Sketch:wght@700&display=swap">
<style>
:root{
  --red:#b3120d;
  --red-deep:#8c0b06;
  --red-bright:#d8211c;
  --band-red:#b71d18;
  --gold:#f6c21a;
  --chalk-gold:#f2b51c;
  --orange:#f0a43a;
  --ink:#141414;
  --nav:#2a2a2a;
  --cream:#f1dcb4;
  --white:#ffffff;
}
*{box-sizing:border-box;margin:0;padding:0}
html,body{width:1007px;height:1200px;overflow:hidden;background:var(--ink)}
body{font-family:"Cutive",serif;color:var(--white);position:relative}
.hero{position:absolute;left:0;top:0;width:1007px;height:590px;
  background:radial-gradient(ellipse at 60% 55%,#c62a14 0%,var(--red) 45%,var(--red-deep) 100%)}
.hero-art{position:absolute;left:0;top:0;width:1007px;height:590px}
.art-bulbs{position:absolute;left:555px;top:0;width:440px;height:360px;
  background:radial-gradient(ellipse at 50% 55%,rgba(246,194,26,.35) 0%,rgba(246,194,26,.12) 45%,rgba(0,0,0,0) 72%)}
.art-bubbles{position:absolute;left:325px;top:405px;width:215px;height:135px;
  background:radial-gradient(ellipse at 50% 50%,rgba(241,220,180,.28) 0%,rgba(241,220,180,.08) 50%,rgba(0,0,0,0) 75%)}
.art-hand{position:absolute;left:720px;top:470px;width:287px;height:120px;
  background:radial-gradient(ellipse at 70% 75%,rgba(240,164,58,.65) 0%,rgba(240,164,58,.25) 45%,rgba(0,0,0,0) 75%)}
.hero-title{position:absolute;left:0;top:0;font-family:"Cabin Sketch",sans-serif;font-weight:700}
.hero-title .line1{position:absolute;left:126px;top:282px;font-size:66px;color:var(--cream);white-space:nowrap;letter-spacing:1px}
.hero-title .line2{position:absolute;left:550px;top:362px;font-size:96px;color:var(--chalk-gold);white-space:nowrap}
.topbar{position:absolute;left:0;top:0;width:1007px;height:68px}
.call{position:absolute;left:82px;top:22px;display:flex;align-items:center;gap:8px}
.call-icon{width:27px;height:27px;border:2px solid var(--white);border-radius:50%;display:flex;align-items:center;justify-content:center}
.call small{display:block;color:var(--gold);font-size:10px}
.call strong{display:block;font-size:14px;font-weight:400;letter-spacing:.5px}
.enroll{position:absolute;left:777px;top:20px;width:147px;height:33px;background:var(--orange);
  border-radius:4px;color:var(--white);font-size:12px;display:flex;align-items:center;justify-content:center;letter-spacing:1px;box-shadow:0 2px 0 #b56a17}
.nav{position:absolute;left:0;top:68px;width:1007px;height:45px;background:var(--nav);
  border-top:1px solid #444;border-bottom:1px solid #111}
.nav a{position:absolute;top:13px;color:var(--white);text-decoration:none;font-size:15px;letter-spacing:.5px}
.nav a.active{color:var(--gold)}
.brand{position:absolute;left:434px;top:27px;width:138px;height:138px;border-radius:50%;background:var(--white);
  display:flex;align-items:center;justify-content:center;text-align:center;color:var(--red-deep);font-size:17px;line-height:1.1}
.welcome{position:absolute;left:0;top:590px;width:1007px;height:400px;
  background:radial-gradient(ellipse at 50% 30%,#3b3b3b 0%,#1c1c1c 60%,#0c0c0c 100%)}
.frame{position:absolute;left:83px;top:46px;width:840px;height:312px;border:1px dotted #cfcfcf}
.welcome h1{position:absolute;left:0;top:84px;width:1007px;text-align:center;font-weight:400;font-size:29px;line-height:36px;letter-spacing:.5px}
.welcome h1 .r{color:#e1141a}
.welcome h1 .y{color:var(--gold)}
.welcome p{position:absolute;left:130px;top:130px;width:747px;text-align:center;font-size:12.4px;line-height:23.4px;color:#eee}
.more{position:absolute;left:470px;top:325px;width:67px;height:34px;border-radius:34px 34px 0 0;background:#4a4a4a;display:flex;justify-content:center;align-items:center}
.share{position:absolute;left:0;top:990px;width:1007px;height:90px;background:var(--band-red)}
.share-note{position:absolute;left:288px;top:22px;font-family:"Caveat",cursive;font-size:17px;line-height:17px;transform:rotate(-14deg)}
.share svg{position:absolute;left:348px;top:30px}
.social{position:absolute;top:24px;width:40px;height:40px;border-radius:50%;border:2px solid var(--white);background:var(--red-bright);
  display:flex;align-items:center;justify-content:center;font-size:9px;letter-spacing:.3px;color:var(--white)}
.contact{position:absolute;left:0;top:1080px;width:1007px;height:77px;background:#a51813}
.contact-item{position:absolute;top:22px;display:flex;gap:10px}
.badge{width:31px;height:31px;border-radius:50%;background:var(--gold);display:flex;align-items:center;justify-content:center;flex:none}
.contact-item b{display:block;font-size:11px;font-weight:400;letter-spacing:1px}
.contact-item span{display:block;font-size:12px;margin-top:3px;white-space:nowrap}
.footer{position:absolute;left:0;top:1157px;width:1007px;height:43px;background:#000;text-align:center;line-height:43px;font-size:11px;color:#ddd}
.footer strong{color:var(--white);font-weight:400}
</style>
</head>
<body>
<section class="hero">
  <div class="hero-art" role="img" aria-label="Chalk drawing of hanging light bulbs, two speech bubbles and a hand holding chalk">
    <div class="art-bulbs"></div>
    <div class="art-bubbles"></div>
    <div class="art-hand"></div>
  </div>
  <h2 class="hero-title"><span class="line1">Do you speak</span><span class="line2">chinese ?</span></h2>
  <div class="topbar">
    <div class="call">
      <div class="call-icon"><svg width="13" height="13" viewBox="0 0 24 24"><path fill="#f6c21a" d="M6.6 10.8a15 15 0 0 0 6.6 6.6l2.2-2.2c.3-.3.7-.4 1-.2 1.1.4 2.3.6 3.6.6.6 0 1 .4 1 1V20c0 .6-.4 1-1 1A17 17 0 0 1 3 4c0-.6.4-1 1-1h3.5c.6 0 1 .4 1 1 0 1.3.2 2.5.6 3.6.1.3 0 .7-.2 1z"/></svg></div>
      <div><small>Call Us Anytime</small><strong>123-456-7890</strong></div>
    </div>
    <div class="enroll">ENROLL NOW!</div>
  </div>
  <nav class="nav">
    <a class="active" style="left:124px">HOME</a>
    <a style="left:231px">OUR SERVICES</a>
    <a style="left:633px">NEWS ROOM</a>
    <a style="left:795px">CONTACT US</a>
  </nav>
  <div class="brand">Jadeway<br>Mandarin</div>
</section>

<section class="welcome">
  <div class="frame"></div>
  <h1>WELCOME TO <span class="r">JADEWAY</span> <span class="y">MANDARIN</span></h1>
  <p>Lorem ipsum dolor sit amet, consectetuer adipiscing elit, sed diam nonummy nibh euismod tincidunt ut laoreet dolore magna aliquam erat volutpat. Ut wisi enim ad minim veniam, quis nostrud exerci tation ullamcorper suscipit lobortis nisl ut aliquip ex ea commodo consequat. Duis autem vel eum iriure dolor in hendrerit in vulputate velit esse molestie consequat, vel illum dolore eu feugiat nulla facilisis at vero eros et accumsan et iusto odio dignissim qui blandit praesent luptatum zzril delenit augue duis dolore te feugait nulla facilisi. Lorem ipsum dolor sit amet, consectetuer adipiscing elit, sed diam nonummy nibh euismod tincidunt ut laoreet dolore magna aliquam erat volutpat. Ut wisi enim ad minim veniam.</p>
  <div class="more"><svg width="16" height="10" viewBox="0 0 16 10"><path d="M1 1l7 7 7-7" fill="none" stroke="#fff" stroke-width="2"/></svg></div>
</section>

<section class="share">
  <div class="share-note">Sharing Is<br>Caring!</div>
  <svg width="92" height="24" viewBox="0 0 92 24"><path d="M2 14c25 10 55 6 86-6" fill="none" stroke="#fff" stroke-width="2"/><path d="M80 4l9 4-6 8" fill="none" stroke="#fff" stroke-width="2"/></svg>
  <div class="social" style="left:452px">Share</div>
  <div class="social" style="left:529px">Post</div>
  <div class="social" style="left:605px">Link</div>
  <div class="social" style="left:682px">Chat</div>
</section>

<section class="contact">
  <div class="contact-item" style="left:101px">
    <div class="badge"><svg width="12" height="15" viewBox="0 0 12 16"><path fill="#6b1a0c" d="M6 0a6 6 0 0 0-6 6c0 4.5 6 10 6 10s6-5.5 6-10a6 6 0 0 0-6-6zm0 8.5A2.5 2.5 0 1 1 6 3.5a2.5 2.5 0 0 1 0 5z"/></svg></div>
    <div><b>JADEWAY MANDARIN</b><span>123, Lorem Dolor zipcode -123 456</span></div>
  </div>
  <div class="contact-item" style="left:405px">
    <div class="badge"><svg width="13" height="13" viewBox="0 0 24 24"><path fill="#6b1a0c" d="M6.6 10.8a15 15 0 0 0 6.6 6.6l2.2-2.2c.3-.3.7-.4 1-.2 1.1.4 2.3.6 3.6.6.6 0 1 .4 1 1V20c0 .6-.4 1-1 1A17 17 0 0 1 3 4c0-.6.4-1 1-1h3.5c.6 0 1 .4 1 1 0 1.3.2 2.5.6 3.6.1.3 0 .7-.2 1z"/></svg></div>
    <div><b>CALL US :</b><span>123-456-7890</span></div>
  </div>
  <div class="contact-item" style="left:579px">
    <div class="badge"><svg width="14" height="13" viewBox="0 0 14 13"><rect x="3" y="0" width="8" height="4" fill="#6b1a0c"/><rect x="0" y="4" width="14" height="6" rx="1" fill="#6b1a0c"/><rect x="3" y="8" width="8" height="5" fill="#6b1a0c" stroke="#f6c21a"/></svg></div>
    <div><b>FAX US :</b><span>123-456-7890</span></div>
  </div>
  <div class="contact-item" style="left:753px">
    <div class="badge"><svg width="14" height="10" viewBox="0 0 14 10"><rect width="14" height="10" fill="#6b1a0c"/><path d="M0 0l7 6 7-6" fill="none" stroke="#f6c21a"/></svg></div>
    <div><b>EMAIL US:</b><span>info@jadewaymandarin.com</span></div>
  </div>
</section>

<footer class="footer">Copyright © 2016 <strong>Jadeway Mandarin</strong> | All Rights Reserved</footer>
</body>
</html>
```